Business Card Design

We are a business based in Sydney repairing and restoring timber windows. We mainly cater to residential home owners although sometimes work with larger building companies. We do a lot of work in heritage buildings though also cater to modern windows.
Our Logo is Black and Gold and were thinking of using a white card with only these two colours although we are open to any design suggestions. Check out our website for ideas.
Front of Card
Contact Information, Website & Business Name
Back of Card
Business Logo, website?
Target Market(s)
Home Owners
Industry/Entity Type
Residential
Contact Information for Business Card
Oakridge Sash Revivals
Marcus Pellow
0472 309 648
marcus@oakridgesashrevivals.example
www.oakridgesashrevivals.example
Look and feel

```html
<!DOCTYPE html>
<html lang="en">
<head>
<meta charset="utf-8">
<title>Oakridge Sash Revivals – Business Card</title>
<link href="https://fonts.googleapis.com/css2?family=Lobster+Two:wght@700&family=Open+Sans:wght@400;600&display=swap" rel="stylesheet">
<style>
  :root {
    --gold: #e2b91f;
    --gold-deep: #c99d0e;
    --gold-light: #f1d45a;
    --ink: #2b2b2b;
    --grey: #9a9a9a;
    --grey-light: #d6d6d6;
    --white: #ffffff;
    --paper: #f4f4f4;
    --backdrop: #e9e6e1;
  }
  html, body {
    margin: 0;
    padding: 0;
    width: 704px;
    height: 1200px;
    overflow: hidden;
    background: var(--backdrop);
  }
  .canvas {
    position: relative;
    width: 704px;
    height: 1200px;
  }
  .card {
    position: absolute;
    left: 52px;
    width: 600px;
    height: 343px;
    border-radius: 14px;
    overflow: hidden;
    box-shadow: 0 6px 18px rgba(0,0,0,0.18);
    font-family: "Open Sans", sans-serif;
  }
  .card--back { top: 150px; background: var(--gold); }
  .card--front { top: 680px; background: linear-gradient(180deg, var(--white), var(--paper)); }

  .wordmark {
    position: absolute;
    font-family: "Lobster Two", cursive;
    font-weight: 700;
    color: var(--ink);
    line-height: 0.95;
    margin: 0;
  }

  /* back side */
  .card--back .wordmark { left: 36px; top: 96px; font-size: 46px; }
  .back-panel {
    position: absolute;
    left: 0; top: 0;
    width: 600px; height: 343px;
  }
  .map-area {
    position: absolute;
    right: 36px; top: 26px;
    width: 230px; height: 140px;
    border: 5px solid var(--white);
    background: linear-gradient(135deg, #e8e4d6, #cfd9c4 55%, #d9d3c0);
  }
  .service-strip {
    position: absolute;
    right: 20px; bottom: 24px;
    display: flex;
    gap: 14px;
  }
  .service {
    width: 76px;
    text-align: center;
  }
  .service-photo {
    height: 58px;
    border-radius: 5px;
    background: linear-gradient(160deg, #cdd6de, #8d9aa6);
  }
  .service-photo--brick { background: linear-gradient(160deg, #d7b9a4, #9a6a54); }
  .service-photo--room { background: linear-gradient(160deg, #f1ece6, #c9bfb4); }
  .service-label {
    margin-top: 5px;
    font-size: 7px;
    font-weight: 600;
    letter-spacing: 0.4px;
    color: var(--ink);
    text-transform: uppercase;
  }

  /* front side */
  .card--front .wordmark { left: 38px; top: 52px; font-size: 44px; }
  .front-decor {
    position: absolute;
    left: 0; top: 0;
    width: 600px; height: 343px;
  }
  .contact {
    position: absolute;
    left: 40px; top: 222px;
    font-size: 13px;
    line-height: 1.55;
    color: var(--ink);
  }
  .contact p { margin: 0; }
  .person {
    position: absolute;
    right: 96px; top: 40px;
    text-align: right;
  }
  .person-name {
    margin: 0;
    font-size: 19px;
    color: var(--gold-deep);
    font-weight: 400;
  }
  .person-role {
    margin: 2px 0 0;
    font-size: 13px;
    color: var(--ink);
  }
</style>
</head>
<body>
<main class="canvas">

  <section class="card card--back" aria-label="Back of card">
    <svg class="back-panel" viewBox="0 0 600 343" aria-hidden="true">
      <path d="M260 200 C330 192 420 190 600 186 L600 343 L230 343 Z" fill="var(--white)"/>
      <path d="M230 343 L260 200 C330 192 420 190 600 186" fill="none" stroke="var(--gold-light)" stroke-width="3"/>
    </svg>
    <h2 class="wordmark">Oakridge<br>Sash<br>Revivals</h2>
    <div class="map-area" role="img" aria-label="Street map of the service area"></div>
    <div class="service-strip">
      <figure class="service" style="margin:0">
        <div class="service-photo service-photo--brick" role="img" aria-label="Photo of a restored heritage window"></div>
        <figcaption class="service-label">Restoration</figcaption>
      </figure>
      <figure class="service" style="margin:0">
        <div class="service-photo" role="img" aria-label="Photo of window maintenance"></div>
        <figcaption class="service-label">Maintenance</figcaption>
      </figure>
      <figure class="service" style="margin:0">
        <div class="service-photo" role="img" aria-label="Photo of window glass"></div>
        <figcaption class="service-label">Glass</figcaption>
      </figure>
      <figure class="service" style="margin:0">
        <div class="service-photo service-photo--room" role="img" aria-label="Photo of a replaced sash window in a bright room"></div>
        <figcaption class="service-label">Sash Replacement</figcaption>
      </figure>
    </div>
  </section>

  <section class="card card--front" aria-label="Front of card">
    <svg class="front-decor" viewBox="0 0 600 343" aria-hidden="true">
      <!-- divider bars under the wordmark -->
      <rect x="40" y="194" width="150" height="5" fill="var(--gold)"/>
      <rect x="194" y="194" width="90" height="5" fill="var(--grey-light)"/>
      <rect x="288" y="194" width="70" height="5" fill="var(--grey)"/>
      <!-- right-hand swoosh -->
      <path d="M600 0 L556 0 C520 90 520 250 560 343 L600 343 Z" fill="var(--ink)"/>
      <path d="M556 0 C520 90 520 250 560 343" fill="none" stroke="var(--grey)" stroke-width="10"/>
      <path d="M541 0 C506 90 506 250 546 343" fill="none" stroke="var(--gold)" stroke-width="4"/>
      <!-- rule under the name -->
      <rect x="360" y="98" width="146" height="4" fill="var(--ink)"/>
      <!-- guarantee seal -->
      <circle cx="430" cy="160" r="36" fill="var(--gold-deep)"/>
      <circle cx="430" cy="160" r="29" fill="var(--gold-light)"/>
    </svg>
    <h1 class="wordmark">Oakridge<br>Sash<br>Revivals</h1>
    <div class="person">
      <p class="person-name">Marcus Pellow</p>
      <p class="person-role">Owner</p>
    </div>
    <div class="contact">
      <p>0472 309 648</p>
      <p>marcus@oakridgesashrevivals.example</p>
      <p>www.oakridgesashrevivals.example</p>
    </div>
  </section>

</main>
</body>
</html>
```